Staffing Company Website

We need a website for a new company based out of central California called "Harbor Field Staffing". We staff truck drivers for agriculture trucking businesses. We don't want a super corporate feel, we want something that feels more inviting to the kind of person who would work in Agriculture/Trucking while still being professional. Please let me know if you have any questions

```html
<!DOCTYPE html>
<html lang="en">
<head>
<meta charset="utf-8">
<title>Harbor Field Staffing</title>
<link href="https://fonts.googleapis.com/css2?family=Montserrat:wght@500;600;700;800&family=Open+Sans:wght@400;600&display=swap" rel="stylesheet">
<style>
:root{
  --green:#2f9e3f;
  --green-dark:#1f7a2d;
  --green-deep:#14501d;
  --green-pale:#e6f4e3;
  --ink:#1d1d1d;
  --muted:#7a7a7a;
  --line:#e3e3e3;
  --white:#ffffff;
  --black:#0b0b0b;
  --orange:#f2a33a;
}
*{box-sizing:border-box;margin:0;padding:0}
html,body{width:1200px;height:3356px;overflow:hidden;background:var(--white)}
body{position:relative;font-family:"Open Sans",Arial,sans-serif;color:var(--ink)}
h1,h2,h3,h4,.btn,.nav a,.brand{font-family:"Montserrat",Arial,sans-serif}
.abs{position:absolute}
.btn{display:inline-flex;align-items:center;gap:10px;background:var(--green);color:var(--white);font-weight:700;font-size:13px;padding:10px 12px 10px 22px;border-radius:24px;text-transform:uppercase;letter-spacing:.3px;white-space:nowrap}
.btn .dot{width:22px;height:22px;border-radius:50%;background:var(--white);display:inline-flex;align-items:center;justify-content:center}
.btn.light{background:var(--white);color:var(--green)}
.btn.light .dot{background:var(--green)}

/* hero */
.hero{left:0;top:0;width:1200px;height:720px;overflow:hidden}
.hero-photo{position:absolute;inset:0;background:linear-gradient(160deg,#3f5a2c 0%,#6b7f3a 35%,#4a6a2a 60%,#2c4420 100%)}
.hero-shade{position:absolute;inset:0;background:linear-gradient(90deg,rgba(10,25,10,.55),rgba(10,25,10,0) 60%)}
.brand{display:flex;align-items:center;gap:14px;color:var(--white);font-weight:700;font-size:22px;line-height:1.05;text-transform:uppercase}
.brand .mark{width:52px;height:52px;border-radius:50%;background:var(--white);flex:none}
.hero .brand{position:absolute;left:140px;top:48px}
.nav{position:absolute;left:488px;top:98px;display:flex;gap:28px}
.nav a{color:var(--white);text-decoration:none;font-size:14px;font-weight:600}
.nav a.active{border-bottom:2px solid var(--white);padding-bottom:4px}
.call{position:absolute;left:872px;top:40px;display:flex;align-items:center;gap:10px;color:var(--white)}
.call .ico{width:38px;height:38px;border-radius:50%;background:var(--green);display:flex;align-items:center;justify-content:center}
.call small{display:block;font-size:11px;font-weight:600}
.call b{font-family:"Montserrat",sans-serif;font-size:15px}
.search{position:absolute;left:1012px;top:94px;width:30px;height:30px;border-radius:50%;background:var(--green);display:flex;align-items:center;justify-content:center}
.hero h1{position:absolute;left:140px;top:270px;color:var(--white);font-size:50px;font-weight:800;line-height:1.1;width:560px;text-transform:uppercase}
.hero .btn{position:absolute;left:140px;top:420px}
.hero-wave{position:absolute;left:0;top:580px}
.badge{left:870px;top:560px;width:250px;height:250px;border-radius:50%;background:var(--white);display:flex;align-items:center;justify-content:center;box-shadow:0 6px 20px rgba(0,0,0,.15);z-index:2}
.badge span{font-family:"Montserrat",sans-serif;font-weight:700;font-size:22px;color:var(--green);text-align:center;text-transform:uppercase;line-height:1.2}

/* about */
.about-art{left:130px;top:820px;width:380px;height:380px;border-radius:50% 8px 50% 8px;background:linear-gradient(135deg,#6f9a3e,#3d6a2a 55%,#8fb06a)}
.about-rule{left:560px;top:880px;width:2px;height:300px;background:var(--line)}
.about h2{left:590px;top:820px;font-size:48px;font-weight:800}
h2 .accent,.title .accent{color:var(--green)}
.about p{left:590px;top:892px;width:500px;font-size:15px;line-height:1.75;color:#555}
.about .btn{left:590px;top:1150px}

/* jobs */
.jobs-bg{left:0;top:1290px;width:1200px;height:620px;background:linear-gradient(180deg,#ffffff 0%,var(--green-pale) 45%,#ffffff 100%)}
.title{position:absolute;left:0;width:1200px;text-align:center;font-family:"Montserrat",sans-serif;font-weight:800;font-size:48px;text-transform:uppercase}
.jobs-title{top:1400px}
.jobs-grid{left:152px;top:1510px;width:908px;display:grid;grid-template-columns:repeat(3,1fr);gap:20px 22px}
.job{background:var(--white);border-radius:10px;padding:18px 18px 16px;box-shadow:0 4px 14px rgba(0,0,0,.07);height:120px}
.job.featured{background:#d8edd3}
.job-head{display:flex;justify-content:space-between;align-items:center}
.job h4{font-size:13px;font-weight:700}
.job .tags{display:flex;gap:6px}
.job .tags i{width:16px;height:16px;border-radius:50%;background:var(--orange);display:block}
.job .tags i+i{background:#bdbdbd}
.job p{margin-top:10px;font-size:12px;line-height:1.5;color:#777}
.job .meta{margin-top:10px;display:flex;gap:18px;font-size:11px;color:#666}
.job .meta span::before{content:"";display:inline-block;width:8px;height:8px;border-radius:50%;background:var(--green);margin-right:6px}
.jobs-more{left:504px;top:1828px;padding:10px 12px 10px 26px}

/* blog */
.blog-title{top:2054px}
.blog-grid{left:144px;top:2148px;width:916px;height:494px;display:grid;grid-template-columns:repeat(3,1fr);grid-template-rows:repeat(2,1fr)}
.photo{background:linear-gradient(140deg,#5b7f96,#c7a46b 55%,#3a5a2a)}
.photo.field{background:linear-gradient(140deg,#7fa3c6,#8aa35a 55%,#3c5a26)}
.photo.yard{background:linear-gradient(140deg,#9fb7cf,#6e8f52 50%,#2f5a2d)}
.post{padding:28px 30px;text-align:center}
.post.green{background:var(--green);color:var(--white)}
.post h3{font-size:17px;font-weight:800;text-transform:uppercase}
.post .date{margin-top:8px;font-size:12px;color:var(--orange);font-weight:600}
.post.green .date{color:var(--white)}
.post p{margin-top:12px;font-size:12.5px;line-height:1.6;color:#777}
.post.green p{color:#e7f5e5}
.post .btn{margin-top:16px}
.post.plain .btn{margin-top:18px}

/* contact */
.contact{left:232px;top:2712px;width:728px;height:378px;display:flex;box-shadow:0 6px 24px rgba(0,0,0,.1)}
.contact-info{width:248px;background:var(--green);color:var(--white)}
.contact-info h4{background:var(--green-dark);padding:22px 30px;font-size:15px;font-weight:700;text-transform:uppercase}
.info-row{display:flex;gap:14px;padding:20px 30px 0}
.info-row .ico{width:18px;flex:none}
.info-row b{font-family:"Montserrat",sans-serif;font-size:13px;display:block;text-transform:uppercase}
.info-row span{font-size:12px;line-height:1.6;display:block;margin-top:6px}
.contact-form{flex:1;background:var(--white);padding:22px 32px}
.contact-form h4{font-size:15px;font-weight:700;text-transform:uppercase}
.field{border-bottom:1px solid var(--line);font-size:12px;color:#999;padding:24px 0 8px}
.field.msg{height:96px}
.form-foot{display:flex;justify-content:space-between;align-items:center;margin-top:24px}
.captcha{width:180px;height:48px;border:1px solid var(--line);background:#f8f8f8;display:flex;align-items:center;gap:10px;padding:0 12px;font-size:12px;color:#555}
.captcha i{width:20px;height:20px;border:2px solid #bbb;background:var(--white);display:block}

/* footer */
.footer{left:0;top:3100px;width:1200px;height:256px}
.footer .brand{position:absolute;left:140px;top:84px;font-size:24px}
.socials{position:absolute;left:512px;top:84px;display:flex;gap:14px}
.socials i{width:32px;height:32px;border-radius:50%;background:var(--white);display:block}
.foot-nav{position:absolute;left:512px;top:136px;display:flex;gap:26px}
.foot-nav a{color:var(--white);font-family:"Montserrat",sans-serif;font-size:14px;font-weight:600;text-decoration:none}
.copy{position:absolute;left:512px;top:178px;color:#cfcfcf;font-size:12px}
</style>
</head>
<body>

<header class="abs hero">
  <div class="hero-photo" role="img" aria-label="Aerial view of a harvester and truck working in a green crop field"></div>
  <div class="hero-shade"></div>
  <div class="brand"><span class="mark"></span><span>Harbor<br>Field<br>Staffing</span></div>
  <div class="call">
    <span class="ico"><svg width="16" height="16" viewBox="0 0 24 24" fill="#fff"><path d="M6.6 10.8a15 15 0 0 0 6.6 6.6l2.2-2.2a1 1 0 0 1 1-.25 11.4 11.4 0 0 0 3.6.57 1 1 0 0 1 1 1V20a1 1 0 0 1-1 1A17 17 0 0 1 3 4a1 1 0 0 1 1-1h3.5a1 1 0 0 1 1 1 11.4 11.4 0 0 0 .57 3.6 1 1 0 0 1-.25 1z"/></svg></span>
    <div><small>CALL US</small><b>+1 000 000 0000</b></div>
  </div>
  <nav class="nav">
    <a class="active">HOME</a><a>ABOUT US</a><a>SERVICES</a><a>NEWS</a><a>CONTACT US</a>
  </nav>
  <span class="search"><svg width="14" height="14" viewBox="0 0 24 24" fill="none" stroke="#fff" stroke-width="3"><circle cx="10" cy="10" r="6"/><path d="M15 15l6 6"/></svg></span>
  <h1>Harbor Field Staffing</h1>
  <span class="btn">Get Started <span class="dot"><svg width="10" height="10" viewBox="0 0 10 10"><path d="M3 1l4 4-4 4" stroke="#2f9e3f" stroke-width="2" fill="none"/></svg></span></span>
  <svg class="hero-wave" width="1200" height="140" viewBox="0 0 1200 140">
    <path d="M0 70 C300 150 700 150 1200 30 L1200 140 L0 140Z" fill="#2f9e3f"/>
    <path d="M0 100 C320 160 760 150 1200 70 L1200 140 L0 140Z" fill="#ffffff"/>
  </svg>
</header>
<div class="abs badge"><span>Harbor<br>Field</span></div>

<section class="about">
  <div class="abs about-art" role="img" aria-label="Collage of farm fields and trucks shaped as a leaf"></div>
  <div class="abs about-rule"></div>
  <h2 class="abs">ABOUT <span class="accent">US</span></h2>
  <p class="abs">Sed ut perspiciatis unde omnis iste natus error sit voluptatem accusantium doloremque laudantium, totam rem aperiam, eaque ipsa quae ab illo inventore veritatis et quasi architecto beatae vitae dicta sunt explicabo. Nemo enim ipsam voluptatem quia voluptas sit aspernatur aut odit aut fugit, sed quia consequuntur magni dolores eos qui ratione voluptatem sequi nesciunt. Neque porro quisquam est, qui dolorem ipsum quia dolor sit amet, consectetur, adipisci velit, sed quia non numquam eius modi tempora ut labore magnam aliquam quaerat voluptatem.</p>
  <span class="abs btn">Read More <span class="dot"><svg width="10" height="10" viewBox="0 0 10 10"><path d="M3 1l4 4-4 4" stroke="#2f9e3f" stroke-width="2" fill="none"/></svg></span></span>
</section>

<section class="jobs">
  <div class="abs jobs-bg"></div>
  <h2 class="title jobs-title">JOB <span class="accent">OPPORTUNITIES</span></h2>
  <div class="abs jobs-grid">
    <article class="job"><div class="job-head"><h4>SED QUIA NON NUMQ</h4><div class="tags"><i></i><i></i></div></div><p>Sed ut perspiciatis unde omnis iste natus error sit voluptatem.</p><div class="meta"><span>Full Time</span><span>2 Days ago</span></div></article>
    <article class="job featured"><div class="job-head"><h4>SED QUIA NON NUMQ</h4><div class="tags"><i></i><i></i></div></div><p>Sed ut perspiciatis unde omnis iste natus error sit voluptatem.</p><div class="meta"><span>Full Time</span><span>2 Days ago</span></div></article>
    <article class="job"><div class="job-head"><h4>SED QUIA NON NUMQ</h4><div class="tags"><i></i><i></i></div></div><p>Sed ut perspiciatis unde omnis iste natus error sit voluptatem.</p><div class="meta"><span>Full Time</span><span>2 Days ago</span></div></article>
    <article class="job"><div class="job-head"><h4>SED QUIA NON NUMQ</h4><div class="tags"><i></i><i></i></div></div><p>Sed ut perspiciatis unde omnis iste natus error sit voluptatem.</p><div class="meta"><span>Full Time</span><span>2 Days ago</span></div></article>
    <article class="job"><div class="job-head"><h4>SED QUIA NON NUMQ</h4><div class="tags"><i></i><i></i></div></div><p>Sed ut perspiciatis unde omnis iste natus error sit voluptatem.</p><div class="meta"><span>Full Time</span><span>2 Days ago</span></div></article>
    <article class="job"><div class="job-head"><h4>SED QUIA NON NUMQ</h4><div class="tags"><i></i><i></i></div></div><p>Sed ut perspiciatis unde omnis iste natus error sit voluptatem.</p><div class="meta"><span>Full Time</span><span>2 Days ago</span></div></article>
  </div>
  <span class="abs btn jobs-more">Load More Jobs <span class="dot"><svg width="10" height="10" viewBox="0 0 10 10"><path d="M3 1l4 4-4 4" stroke="#2f9e3f" stroke-width="2" fill="none"/></svg></span></span>
</section>

<section class="blog">
  <h2 class="title blog-title">FROM <span class="accent">THE BLOG</span></h2>
  <div class="abs blog-grid">
    <div class="photo" role="img" aria-label="Truck driver standing beside a yellow truck"></div>
    <article class="post green"><h3>At Vero Eos Eaccusamu</h3><div class="date">Jan 10,2024</div><p>At vero eos et accusamus et iusto odio dignissimos ducimus qui blanditiis praesentium voluptatum.</p><span class="btn light">Read More <span class="dot"><svg width="10" height="10" viewBox="0 0 10 10"><path d="M3 1l4 4-4 4" stroke="#fff" stroke-width="2" fill="none"/></svg></span></span></article>
    <div class="photo yard" role="img" aria-label="Workers talking together outside a farm building"></div>
    <article class="post plain"><h3>At Vero Eos Eaccusamu</h3><div class="date">Jan 10,2024</div><p>At vero eos et accusamus et iusto odio dignissimos ducimus qui blanditiis praesentium voluptatum.</p><span class="btn">Read More <span class="dot"><svg width="10" height="10" viewBox="0 0 10 10"><path d="M3 1l4 4-4 4" stroke="#2f9e3f" stroke-width="2" fill="none"/></svg></span></span></article>
    <div class="photo field" role="img" aria-label="Farm worker in a hat standing in a crop field"></div>
    <article class="post plain"><h3>At Vero Eos Eaccusamu</h3><div class="date">Jan 10,2024</div><p>At vero eos et accusamus et iusto odio dignissimos ducimus qui blanditiis praesentium voluptatum.</p><span class="btn">Read More <span class="dot"><svg width="10" height="10" viewBox="0 0 10 10"><path d="M3 1l4 4-4 4" stroke="#2f9e3f" stroke-width="2" fill="none"/></svg></span></span></article>
  </div>
</section>

<section class="abs contact">
  <div class="contact-info">
    <h4>Get In Touch</h4>
    <div class="info-row"><svg class="ico" viewBox="0 0 24 24" fill="#fff"><path d="M12 2a7 7 0 0 0-7 7c0 5 7 13 7 13s7-8 7-13a7 7 0 0 0-7-7zm0 9.5A2.5 2.5 0 1 1 12 6.5a2.5 2.5 0 0 1 0 5z"/></svg><div><b>Address</b><span>Sed ullam lorem dolor sit<br>consectetur elit</span></div></div>
    <div class="info-row"><svg class="ico" viewBox="0 0 24 24" fill="#fff"><path d="M6.6 10.8a15 15 0 0 0 6.6 6.6l2.2-2.2a1 1 0 0 1 1-.25 11.4 11.4 0 0 0 3.6.57 1 1 0 0 1 1 1V20a1 1 0 0 1-1 1A17 17 0 0 1 3 4a1 1 0 0 1 1-1h3.5a1 1 0 0 1 1 1 11.4 11.4 0 0 0 .57 3.6 1 1 0 0 1-.25 1z"/></svg><div><b>Phone</b><span>+1 000 000 0000</span></div></div>
    <div class="info-row"><svg class="ico" viewBox="0 0 24 24" fill="#fff"><path d="M3 5h18v14H3z M3 5l9 7 9-7" stroke="#2f9e3f" stroke-width="1.5"/></svg><div><b>Email</b><span>info@companyname.com</span></div></div>
  </div>
  <form class="contact-form">
    <h4>Let's Talk</h4>
    <div class="field">First Name</div>
    <div class="field">Email Address</div>
    <div class="field msg">Message</div>
    <div class="form-foot">
      <div class="captcha"><i></i>I'm not a robot</div>
      <span class="btn">Submit <span class="dot"><svg width="10" height="10" viewBox="0 0 10 10"><path d="M3 1l4 4-4 4" stroke="#2f9e3f" stroke-width="2" fill="none"/></svg></span></span>
    </div>
  </form>
</section>

<footer class="abs footer">
  <svg class="abs" style="left:0;top:0" width="1200" height="256" viewBox="0 0 1200 256">
    <path d="M0 30 C400 0 800 0 1200 30 L1200 256 L0 256Z" fill="#2f9e3f"/>
    <path d="M0 40 C400 12 800 12 1200 40 L1200 256 L0 256Z" fill="#0b0b0b"/>
  </svg>
  <div class="brand"><span class="mark"></span><span>Harbor<br>Field<br>Staffing</span></div>
  <div class="socials"><i></i><i></i><i></i><i></i><i></i></div>
  <nav class="foot-nav"><a>HOME</a><a>ABOUT US</a><a>SERVICES</a><a>NEWS</a><a>CONTACT US</a></nav>
  <p class="copy">Copyright © 2024 Companyname All Rights Reserved &nbsp;|&nbsp; Privacy Policy &nbsp;|&nbsp; Terms of use</p>
</footer>

</body>
</html>
```